Bright Arch Group business card

Bright Arch Group is the parent company of Bright Arch Building, Bright Arch Plumbing and Bright Arch Renovating. We require a sophisticated business card that covers all aspects of the building and plumbing space without using told or construction items.

Industry/Entity Type

Construction Company

Contact Information for Business Card

Gareth Pimley
Director
0472915083
gareth@brightarch.com.au
Www.brightarch.com.au

Font styles to use
Serif
Sans Serif

Colors
3176b5
ffce3e
0692cd
34a7d8
fbee3e
faa54b

Requirements
Must have
• Logo on front
• Logo and details on rear.
Nice to have
• Maybe water mark or shadow effect with logo
Should not have
• Tools or any construction associated items

```html
<!DOCTYPE html>
<html lang="en">
<head>
<meta charset="utf-8">
<title>Bright Arch Group – Business Card</title>
<link rel="stylesheet" href="https://fonts.googleapis.com/css2?family=Cinzel:wght@400;500&family=Questrial&family=Josefin+Sans:wght@300;400;600&display=swap">
<style>
  :root {
    --canvas-bg: #e9e7e4;
    --card-bg: #ffffff;
    --ink: #1d1d1d;
    --ink-soft: #3a3a3a;
    --gold: #eea92f;
    --gold-light: #f6c98c;
    --gold-deep: #e9a04a;
    --card-shadow: rgba(40, 30, 20, 0.18);
  }
  * { margin: 0; padding: 0; box-sizing: border-box; }
  html, body {
    width: 1200px;
    height: 1023px;
    overflow: hidden;
    background: var(--canvas-bg);
  }
  .canvas {
    position: relative;
    width: 1200px;
    height: 1023px;
    display: flex;
    align-items: center;
    justify-content: center;
    gap: 48px;
  }
  .card {
    position: relative;
    width: 530px;
    height: 303px;
    background: var(--card-bg);
    box-shadow: 0 14px 34px var(--card-shadow), 0 2px 6px rgba(0,0,0,0.08);
  }

  /* Details side */
  .card--details .brand-mark {
    position: absolute;
    left: 46px;
    top: 56px;
    width: 190px;
    height: 190px;
    border-radius: 50%;
    background: radial-gradient(circle at 40% 35%, var(--gold-light), var(--gold-deep));
    opacity: 0.85;
  }
  .card--details .identity {
    position: absolute;
    left: 262px;
    top: 82px;
  }
  .identity__name {
    font-family: "Cinzel", serif;
    font-weight: 500;
    font-size: 27px;
    letter-spacing: 0.5px;
    color: var(--ink);
    line-height: 1;
  }
  .identity__role {
    margin-top: 10px;
    margin-left: 118px;
    font-family: "Questrial", sans-serif;
    font-size: 15px;
    color: var(--ink-soft);
    letter-spacing: 0.5px;
  }
  .contact {
    position: absolute;
    left: 262px;
    top: 176px;
    font-family: "Questrial", sans-serif;
    color: var(--ink);
  }
  .contact__phone {
    display: flex;
    align-items: center;
    gap: 8px;
    font-family: "Josefin Sans", sans-serif;
    font-weight: 600;
    font-size: 23px;
    letter-spacing: 0.5px;
  }
  .contact__phone svg { width: 16px; height: 16px; fill: var(--ink); }
  .contact__line {
    font-size: 14.5px;
    letter-spacing: 0.4px;
    margin-top: 6px;
    color: var(--ink-soft);
  }

  /* Logo side */
  .card--logo {
    display: flex;
    align-items: center;
    justify-content: center;
  }
  .logo-lockup {
    display: flex;
    align-items: center;
    gap: 18px;
  }
  .logo-lockup__dot {
    width: 46px;
    height: 46px;
    border-radius: 50%;
    background: var(--gold);
  }
  .logo-lockup__name {
    font-family: "Josefin Sans", sans-serif;
    font-weight: 300;
    font-size: 34px;
    letter-spacing: 7px;
    text-transform: uppercase;
    color: var(--ink);
  }
</style>
</head>
<body>
<main class="canvas">

  <section class="card card--details" aria-label="Business card, details side">
    <div class="brand-mark" aria-hidden="true"></div>
    <div class="identity">
      <h1 class="identity__name">Gareth Pimley</h1>
      <p class="identity__role">Director</p>
    </div>
    <div class="contact">
      <p class="contact__phone">
        <svg viewBox="0 0 24 24" aria-hidden="true"><path d="M6.6 10.8a15.1 15.1 0 0 0 6.6 6.6l2.2-2.2c.3-.3.7-.4 1-.2 1.1.4 2.3.6 3.6.6.6 0 1 .4 1 1V20c0 .6-.4 1-1 1A17 17 0 0 1 3 4c0-.6.4-1 1-1h3.5c.6 0 1 .4 1 1 0 1.3.2 2.5.6 3.6.1.3 0 .7-.2 1L6.6 10.8z"/></svg>
        0472915083
      </p>
      <p class="contact__line">gareth@brightarch.com.au</p>
      <p class="contact__line">www.brightarch.com.au</p>
    </div>
  </section>

  <section class="card card--logo" aria-label="Business card, logo side">
    <div class="logo-lockup">
      <span class="logo-lockup__dot" aria-hidden="true"></span>
      <span class="logo-lockup__name">Bright Arch Group</span>
    </div>
  </section>

</main>
</body>
</html>
```